Präsentationsvorlagen für Baufinanzierungsmakler
Zielgruppe
Ich bin freier Baufinanzierungsmakler und helfe Privatkunden wie auch Selbständigen die für Sie passende Immobilie zu finanzieren.
Aufgabenstellung
Bitte die Designvorlage der bestehenden Präsentation berücksichtigen und evtl. etwas aufpumpen - sofern es Sinn ergibt. Ebenso soll das Wording auf manchen Folien angepasst und 1 Folie zusätzlich eingefügt werden

```html
<!DOCTYPE html>
<html lang="de">
<head>
<meta charset="utf-8">
<title>Brückstein Partner – Präsentationsvorlagen</title>
<link href="https://fonts.googleapis.com/css2?family=Nunito:wght@400;600;800;900&display=swap" rel="stylesheet">
<style>
  :root{
    --yellow:#f7b519;
    --gold:#d9a52a;
    --navy:#002a75;
    --ink:#1e2a4a;
    --stage:#edf1f5;
    --white:#ffffff;
  }
  *{box-sizing:border-box;margin:0;padding:0}
  html,body{width:1200px;height:736px;overflow:hidden;background:var(--stage);font-family:"Nunito",sans-serif;color:var(--ink)}
  .slide{position:absolute;width:339px;height:191px;box-shadow:0 14px 30px rgba(40,70,120,.16);overflow:hidden;background:var(--white)}
  .slide-inner{position:absolute;left:0;top:0;width:696px;height:392px;transform:scale(.4871);transform-origin:0 0}
  .col-1{left:55px}.col-2{left:430px}.col-3{left:806px}
  .row-1{top:46px}.row-2{top:273px}.row-3{top:500px}
  .shape{position:absolute;inset:0}
  .fill-yellow{background:var(--yellow)}
  .fill-navy{background:var(--navy)}
  .fill-gold{background:var(--gold)}
  .photo-office{background:linear-gradient(120deg,#c9cfdc 0%,#e8d6c8 40%,#f3efeb 100%)}
  .photo-city{background:linear-gradient(160deg,#6b7f95 0%,#2f3d4f 55%,#9ba6ad 100%)}
  .photo-team{background:linear-gradient(100deg,#2a2f3a 0%,#7d93ad 45%,#c7d6e3 100%)}
  .photo-desk{background:linear-gradient(90deg,#5c7893,#a9bccb)}
  .photo-bokeh{background:linear-gradient(150deg,#f4e8ee 0%,#e7c8d6 45%,#c7b0d6 100%)}
  .photo-handshake{background:linear-gradient(140deg,#c9962b 0%,#e2b33b 60%,#b88a2a 100%)}
  .photo-dark{background:linear-gradient(140deg,#3a2f28 0%,#6b5444 50%,#2c2622 100%)}
  .photo-gold-desk{background:linear-gradient(150deg,#f0b52a 0%,#e6ab26 60%,#d59d20 100%)}
  .portrait{position:absolute;left:395px;top:147px;width:96px;height:96px;background:linear-gradient(160deg,#dfe6ee,#8c9bad);box-shadow:0 2px 6px rgba(0,0,0,.25);border:2px solid #fff}
  .title{position:absolute;font-weight:900;color:var(--yellow);font-size:30px;line-height:40px;letter-spacing:.3px;text-transform:uppercase}
  .bullets{position:absolute;list-style:none;font-size:12.5px;line-height:28px;color:var(--ink)}
  .bullets li{position:relative;padding-left:16px}
  .bullets li::before{content:"";position:absolute;left:0;top:12px;width:4px;height:4px;background:var(--navy)}
  .bullets.tall li{line-height:22px;margin-bottom:6px}
  .bullets.tall li::before{top:9px}
  .footer{position:absolute;left:0;bottom:0;height:31px;width:100%;display:flex;align-items:center;font-size:10px;color:var(--navy);font-weight:600}
  .footer .num{width:72px;text-align:center;border-right:1px solid var(--navy);line-height:16px;padding-left:4px;margin-right:14px}
  .footer.on-navy{color:#fff}
  .footer.on-navy .num{border-color:#fff}
  .top-band{position:absolute;right:0;top:0;height:30px;display:flex;align-items:center;font-size:10px;font-weight:600;color:var(--navy)}
  .top-band .num{border-left:1px solid var(--navy);padding-left:14px;margin-left:10px;width:70px;line-height:14px}
  .brand-label{position:absolute;left:428px;top:224px;width:202px;height:51px;background:var(--yellow);color:var(--navy);font-weight:800;font-size:20px;display:flex;align-items:center;justify-content:center}
  .cta{position:absolute;left:306px;top:265px;width:197px;height:42px;background:var(--yellow);border-radius:4px;color:#fff;font-weight:900;font-size:14px;letter-spacing:.5px;display:flex;align-items:center;justify-content:center;gap:10px}
  .cta .divider{width:1px;height:22px;background:#fff}
  .contact{position:absolute;left:44px;color:#fff;font-size:13px;line-height:20px}
  .contact dl{display:grid;grid-template-columns:86px 22px auto}
  .thanks-sub{position:absolute;left:44px;top:110px;color:var(--yellow);font-weight:800;font-size:15px}
  .perks{position:absolute;left:44px;top:150px;list-style:none;font-size:12.5px}
  .perks li{display:flex;align-items:center;gap:16px;height:42px}
  .perks .icon{width:24px;height:22px;background:var(--yellow);display:flex;align-items:center;justify-content:center}
</style>
</head>
<body>

<!-- Slide 1: Titel -->
<section class="slide col-1 row-1"><div class="slide-inner">
  <div class="shape photo-office" role="img" aria-label="Geschäftsmann mit Tablet vor Stadtsilhouette" style="clip-path:polygon(0 0,445px 0,280px 247px,0 247px)"></div>
  <div class="shape" role="img" aria-label="Helle, unscharfe Stadtansicht" style="background:linear-gradient(90deg,#fbf6f3,#f1e6e3);clip-path:polygon(445px 0,696px 0,696px 247px,280px 247px)"></div>
  <div class="shape fill-yellow" style="clip-path:polygon(0 247px,302px 247px,193px 392px,0 392px)"></div>
  <div class="shape fill-gold" style="clip-path:polygon(0 247px,250px 247px,220px 290px,0 290px)"></div>
  <div class="shape fill-navy" style="clip-path:polygon(302px 247px,696px 247px,696px 392px,193px 392px)"></div>
  <div class="brand-label">Brückstein Partner</div>
</div></section>

<!-- Slide 2: Über das Unternehmen -->
<section class="slide col-2 row-1"><div class="slide-inner">
  <div class="shape photo-city" role="img" aria-label="Person mit Dokumenten vor nächtlicher Skyline" style="clip-path:polygon(572px 0,696px 0,696px 392px,295px 392px,475px 125px)"></div>
  <div class="shape fill-yellow" style="clip-path:polygon(377px 0,572px 0,475px 125px)"></div>
  <h2 class="title" style="left:44px;top:52px">Über<br>Brückstein Partner:</h2>
  <ul class="bullets" style="left:44px;top:145px">
    <li>Gegründet im Jahr 2007 von Peter Albrecht</li>
    <li>Übernahme Vertrieb und Akquisition von Lukas Bernhagen</li>
    <li>2021 Premium Partner Wohnportal Nord</li>
  </ul>
  <div class="shape fill-yellow" style="clip-path:polygon(0 361px,500px 361px,480px 392px,0 392px)"></div>
  <div class="footer"><span class="num">2</span>www.brueckstein-partner.de</div>
</div></section>

<!-- Slide 3: Über das Unternehmen, Zahlen -->
<section class="slide col-3 row-1"><div class="slide-inner">
  <div class="shape photo-city" role="img" aria-label="Person mit Dokumenten vor nächtlicher Skyline" style="clip-path:polygon(572px 0,696px 0,696px 392px,295px 392px,475px 125px)"></div>
  <div class="shape fill-yellow" style="clip-path:polygon(377px 0,572px 0,475px 125px)"></div>
  <h2 class="title" style="left:44px;top:52px">Über<br>Brückstein Partner:</h2>
  <ul class="bullets" style="left:44px;top:145px">
    <li>Über 500 Bankpartner im Portfolio</li>
    <li>Abgeschlossenes Volumen 2021: ca. 13 Mio. €</li>
    <li style="line-height:22px;padding-top:3px">Abgeschlossenes Volumen 2022: ca. 8 Mio. €<br>(Stand 30. Mai 2022)</li>
  </ul>
  <div class="shape fill-yellow" style="clip-path:polygon(0 361px,500px 361px,480px 392px,0 392px)"></div>
  <div class="footer"><span class="num">3</span>www.brueckstein-partner.de</div>
</div></section>

<!-- Slide 4: Mehrwert I -->
<section class="slide col-1 row-2"><div class="slide-inner">
  <div class="shape photo-team" role="img" aria-label="Silhouetten einer Geschäftsgruppe am Fenster" style="clip-path:polygon(0 0,365px 0,215px 278px,0 278px)"></div>
  <div class="shape photo-desk" role="img" aria-label="Besprechungstisch mit Unterlagen" style="clip-path:polygon(0 278px,215px 278px,125px 392px,0 392px)"></div>
  <div class="shape fill-yellow" style="clip-path:polygon(125px 392px,215px 278px,320px 392px)"></div>
  <div class="shape fill-yellow" style="clip-path:polygon(220px 0,696px 0,696px 30px,200px 30px)"></div>
  <div class="top-band"><span>www.brueckstein-partner.de</span><span class="num">4</span></div>
  <h2 class="title" style="left:366px;top:112px">Unser Mehrwert<br>für Sie:</h2>
  <ul class="bullets" style="left:356px;top:204px">
    <li>Höhere Konvertierung</li>
    <li>Schnelle und termingerechte Bearbeitung</li>
    <li>Hilfe bei der Auswahl der geeigneten Bankpartner</li>
  </ul>
</div></section>

<!-- Slide 5: Mehrwert II -->
<section class="slide col-2 row-2"><div class="slide-inner">
  <div class="shape photo-team" role="img" aria-label="Silhouetten einer Geschäftsgruppe am Fenster" style="clip-path:polygon(0 0,365px 0,215px 278px,0 278px)"></div>
  <div class="shape photo-desk" role="img" aria-label="Besprechungstisch mit Unterlagen" style="clip-path:polygon(0 278px,215px 278px,125px 392px,0 392px)"></div>
  <div class="shape fill-yellow" style="clip-path:polygon(125px 392px,215px 278px,320px 392px)"></div>
  <div class="shape fill-yellow" style="clip-path:polygon(220px 0,696px 0,696px 30px,200px 30px)"></div>
  <div class="top-band"><span>www.brueckstein-partner.de</span><span class="num">5</span></div>
  <h2 class="title" style="left:366px;top:112px">Unser Mehrwert<br>für Sie:</h2>
  <ul class="bullets tall" style="left:356px;top:207px;width:320px">
    <li>Skalierbarkeit bei großen Auftragsvolumen</li>
    <li>Diskretion und Kundenschutz durch uns gegeben (bei Bankpartnern können abweichende Bedingungen gelten)</li>
    <li>Bei entsprechendem Volumen individuelle Lösungen bzgl. der Vertragsgestaltung möglich</li>
  </ul>
</div></section>

<!-- Slide 6: Über die Person -->
<section class="slide col-3 row-2"><div class="slide-inner">
  <div class="shape photo-gold-desk" role="img" aria-label="Schreibtisch mit Unterlagen in Goldton" style="clip-path:polygon(572px 0,696px 0,696px 392px,295px 392px,475px 125px)"></div>
  <div class="shape fill-yellow" style="clip-path:polygon(377px 0,572px 0,475px 125px)"></div>
  <h2 class="title" style="left:44px;top:52px">Über Lukas<br>Bernhagen:</h2>
  <ul class="bullets" style="left:44px;top:145px">
    <li>23 Jahre Erfahrung in der Finanzdienstleistungsbranche</li>
    <li>10 Jahre nachweisliche Krediterfahrung</li>
    <li>200 Mio. € abgeschlossenes Kreditvolumen</li>
  </ul>
  <div class="portrait" role="img" aria-label="Porträtfoto des Finanzierungsspezialisten"></div>
  <div class="shape fill-navy" style="clip-path:polygon(0 361px,500px 361px,480px 392px,0 392px)"></div>
  <div class="footer on-navy"><span class="num">6</span>www.brueckstein-partner.de</div>
</div></section>

<!-- Slide 7: Fallbeispiele -->
<section class="slide col-1 row-3"><div class="slide-inner">
  <div class="shape photo-bokeh" role="img" aria-label="Hand schnippt vor unscharfen Lichtern" style="clip-path:polygon(572px 0,696px 0,696px 392px,295px 392px,475px 125px)"></div>
  <div class="shape fill-yellow" style="clip-path:polygon(377px 0,572px 0,475px 125px)"></div>
  <ul class="bullets tall" style="left:44px;top:52px;width:360px">
    <li>Kauf einer in die Jahre gekommenen Produktionshalle inkl. Nebenkosten</li>
    <li>Anschlussfinanzierung eines denkmalgeschützten Mehrfamilienhauses mit einem 66-jährigen selbständigen Darlehensnehmer</li>
    <li>Finanzierung einer Villa in Berlin mit der Maßgabe innerhalb einer Woche eine Darlehensgenehmigung zu bekommen</li>
  </ul>
  <div class="cta">FALLBEISPIELE<span class="divider"></span>
    <svg width="16" height="16" viewBox="0 0 16 16" aria-hidden="true"><circle cx="6.5" cy="6.5" r="5" fill="none" stroke="#fff" stroke-width="1.6"/><line x1="10.2" y1="10.2" x2="15" y2="15" stroke="#fff" stroke-width="1.6"/></svg>
  </div>
  <div class="shape fill-yellow" style="clip-path:polygon(0 361px,500px 361px,480px 392px,0 392px)"></div>
  <div class="footer"><span class="num">7</span>www.brueckstein-partner.de</div>
</div></section>

<!-- Slide 8: Dank und Kontakt -->
<section class="slide col-2 row-3" style="background:var(--navy)"><div class="slide-inner">
  <div class="shape photo-handshake" role="img" aria-label="Händedruck in warmem Goldton" style="clip-path:polygon(541px 0,696px 0,696px 392px,400px 392px,411px 361px,616px 99px)"></div>
  <h2 class="title" style="left:44px;top:34px;font-size:25px;line-height:35px">Vielen Dank für Ihre<br>Aufmerksamkeit</h2>
  <div class="thanks-sub">LUKAS BERNHAGEN</div>
  <div class="contact" style="top:155px">
    <p style="font-size:15px;margin-bottom:4px">Finanzierungsspezialist</p>
    <p>Brückstein Partner Lukas Bernhagen Lindenweg 14 90402 Musterstadt</p>
  </div>
  <div class="contact" style="top:225px">
    <dl>
      <dt>Telefon</dt><dd>:</dd><dd>+49 911 555 014 00</dd>
      <dt>Fax</dt><dd>:</dd><dd>+49 911 555 014 01</dd>
      <dt>Mobil</dt><dd>:</dd><dd>+49 151 555 207 43</dd>
    </dl>
  </div>
  <div class="contact" style="top:310px">
    <dl>
      <dt>Email</dt><dd>:</dd><dd>lukas.bernhagen@brueckstein-partner.de</dd>
      <dt>Homepage</dt><dd>:</dd><dd>www.brueckstein-partner.de</dd>
    </dl>
  </div>
  <div class="shape fill-yellow" style="clip-path:polygon(0 361px,500px 361px,480px 392px,0 392px)"></div>
  <div class="footer"><span class="num">8</span>www.brueckstein-partner.de</div>
</div></section>

<!-- Slide 9: Vorteile -->
<section class="slide col-3 row-3"><div class="slide-inner">
  <div class="shape photo-dark" role="img" aria-label="Händedruck zweier Geschäftsleute" style="clip-path:polygon(572px 0,696px 0,696px 392px,295px 392px,475px 125px)"></div>
  <div class="shape fill-yellow" style="clip-path:polygon(377px 0,572px 0,475px 125px)"></div>
  <h2 class="title" style="left:44px;top:52px">Vorteile mit mir als<br>freiem Makler</h2>
  <ul class="perks">
    <li><span class="icon"><svg width="14" height="14" viewBox="0 0 14 14" aria-hidden="true"><path d="M1 5 L7 1 L13 5 Z M2 6h10v1H2z M3 8h1v4H3z M6.5 8h1v4h-1z M10 8h1v4h-1z M1 12.5h12v1H1z" fill="#fff"/></svg></span>Unabhängige Beratung</li>
    <li><span class="icon"><svg width="14" height="14" viewBox="0 0 14 14" aria-hidden="true"><circle cx="5" cy="5" r="3.5" fill="none" stroke="#fff" stroke-width="1.2"/><circle cx="9.5" cy="9.5" r="3.5" fill="none" stroke="#fff" stroke-width="1.2"/></svg></span>Maßgeschneiderte Finanzierung</li>
    <li><span class="icon"><svg width="14" height="14" viewBox="0 0 14 14" aria-hidden="true"><path d="M2 11 L7 3 L12 11 Z" fill="none" stroke="#fff" stroke-width="1.2"/><line x1="7" y1="6" x2="7" y2="9" stroke="#fff" stroke-width="1.2"/></svg></span>Zugang zu vielen Banken</li>
  </ul>
  <div class="shape fill-navy" style="clip-path:polygon(0 361px,500px 361px,480px 392px,0 392px)"></div>
  <div class="footer on-navy"><span class="num">9</span>www.brueckstein-partner.de</div>
</div></section>

</body>
</html>
```